Meridian Sound Wellness LLC Card Design

Need business card with a logo for a hearing aid sales and audiology business. We have two Hearing Instrument Specialists and one Audiologist on staff. Over 25 years in business. Locally owned and operated. Financing available. Most insurances accepted.

Meridian Sound Wellness LLC
48730 W Linden Row, Suite 9
Spokane, WA 99481
509-617-2085
www.meridiansoundnorth.example

Manager
Tobias Wrenfield HIS COHC
License #81729046

Target Market(s)

50yr old + people with a hearing loss.

Industry/Entity Type

Business

Contact Information for Business Card

48730 W Linden Row, Suite 9
Spokane, WA 99481
509-617-2085
www.meridiansoundnorth.example

Manager
Tobias Wrenfield HIS COHC
NRPL #81729046

Font styles to use
Serif
Sans Serif

Requirements
Must have
• Business name, Tobias's name and title(s) and contact information, License #, web address
Nice to have
Should not have

```html
<!DOCTYPE html>
<html lang="en">
<head>
<meta charset="utf-8">
<title>Meridian Sound Wellness LLC – Business Card</title>
<link rel="stylesheet" href="https://fonts.googleapis.com/css2?family=Lato:wght@400;700;900&display=swap">
<style>
  :root {
    --backdrop: #e4e7e8;
    --card: #ffffff;
    --ink: #151515;
    --brand-blue: #0a74b5;
    --brand-teal: #0d8f9a;
    --brand-green: #38b54a;
    --on-band: #ffffff;
  }
  * { box-sizing: border-box; margin: 0; padding: 0; }
  html, body {
    width: 960px;
    height: 1200px;
    overflow: hidden;
    background: var(--backdrop);
    font-family: "Lato", Arial, sans-serif;
    color: var(--ink);
  }
  .canvas {
    position: relative;
    width: 960px;
    height: 1200px;
  }
  .card {
    position: absolute;
    left: 40px;
    top: 348px;
    width: 880px;
    height: 503px;
    background: var(--card);
    box-shadow: 0 3px 10px rgba(0,0,0,0.18);
  }
  .brand {
    position: absolute;
    left: 44px;
    top: 40px;
    display: flex;
    align-items: center;
    gap: 22px;
  }
  .brand-dot {
    width: 62px;
    height: 62px;
    border-radius: 50%;
    background: var(--brand-teal);
    flex: none;
  }
  .brand-name {
    font-size: 40px;
    line-height: 40px;
    font-weight: 400;
    color: var(--ink);
  }
  .id-band {
    position: absolute;
    left: 0;
    top: 178px;
    width: 492px;
    height: 140px;
    padding: 12px 0 0 43px;
    background: linear-gradient(90deg, var(--brand-blue) 0%, var(--brand-teal) 45%, var(--brand-green) 100%);
    color: var(--on-band);
    white-space: nowrap;
  }
  .role { font-size: 28px; line-height: 38px; font-weight: 400; }
  .person { font-size: 33px; line-height: 44px; font-weight: 700; }
  .license { font-size: 28px; line-height: 42px; font-weight: 400; }
  .contact {
    position: absolute;
    right: 40px;
    top: 330px;
    text-align: right;
    font-style: normal;
    font-size: 28px;
    line-height: 35.5px;
    white-space: nowrap;
  }
  .contact .web { font-weight: 700; }
  .corner-mark {
    position: absolute;
    left: 40px;
    top: 418px;
  }
</style>
</head>
<body>
  <main class="canvas">
    <section class="card" aria-label="Business card front">
      <header class="brand">
        <span class="brand-dot" aria-hidden="true"></span>
        <h1 class="brand-name">Meridian Sound<br>Wellness LLC</h1>
      </header>

      <div class="id-band">
        <p class="role">Manager</p>
        <p class="person">Tobias Wrenfield HIS COHC</p>
        <p class="license">NRPL #81729046</p>
      </div>

      <address class="contact">
        <p>48730 W Linden Row, Suite 9</p>
        <p>Spokane, WA 99481</p>
        <p>509-617-2085</p>
        <p class="web">www.meridiansoundnorth.example</p>
      </address>

      <svg class="corner-mark" width="46" height="44" viewBox="0 0 46 44" aria-hidden="true">
        <polyline points="2,0 2,42 46,42" fill="none" stroke="#151515" stroke-width="3.5"/>
      </svg>
    </section>
  </main>
</body>
</html>
```